Marrowind Radio needs a functional Internet Radio App

We need a Internet Radio app design for IOS and Android,
Shoutcast/ Icecast Stream( SHOUTcast playlist (.pls) file or Icecast (.m3u) playlist file) Supported streams: AAC, AAC+, HE-AAC+.
Should supports TuneBasket, Virtual Dj, Wowza, Auto Dj
Here are some of the features we need you to include in the design:
1. Multi Stream player with Scheduling
2. Track Display
3. Track Sharing ( Chatterbox and other)
4. Album Cover display( automatic cover retrieval base on track)
5.Track Purchases ( Plunkr and Brivex )
6.Push Notification( Geo-localize outgoing data and schedule messages)
7. News, Podcasts and Videos ( Live Feed)
8. Alarms
9. Incorporate "Dedications" ( Listeners love to see when their message is published in real time)
10.Ad management ( management system for the app)
11.Listeners should be able to 'Skip song'
12. Database for music

Target Market(s)

Everyone

Industry/Entity Type

Radio Station

Font styles to use
Decorative

Colors
3176b5
0355a3
85acd3
ffffff

Requirements
Must have
• 1.I need a functional app
• 2. Song Request
Nice to have
• N/A
Should not have
• Other Radio Station app design

```html
<!DOCTYPE html>
<html lang="en">
<head>
<meta charset="utf-8">
<title>Marrowind Radio – Player Screen</title>
<link rel="stylesheet" href="https://fonts.googleapis.com/css2?family=Arimo:wght@400;700&display=swap">
<style>
  :root{
    --blue:#3176b5;
    --blue-deep:#0355a3;
    --blue-soft:#85acd3;
    --white:#ffffff;
    --cyan:#48c2dc;
    --cyan-mid:#3d9fd6;
    --cyan-text:#5fd3ea;
    --grey-top:#ffffff;
    --grey-bottom:#e6e9ec;
  }
  *{box-sizing:border-box;margin:0;padding:0}
  html,body{width:1098px;height:1200px;overflow:hidden;background:var(--white)}
  body{position:relative;font-family:"Arimo",Arial,sans-serif}
  .app-screen{
    position:absolute;left:214px;top:48px;width:670px;height:1104px;
    border-radius:8px;overflow:hidden;background:var(--grey-bottom);
  }
  .app-header{
    position:absolute;left:0;top:0;width:670px;height:180px;
    background:linear-gradient(180deg,var(--grey-top),var(--grey-bottom));
  }
  .back-button{
    position:absolute;left:46px;top:64px;width:86px;height:26px;
    background:linear-gradient(180deg,var(--cyan-mid),var(--blue));
    color:var(--white);font-size:15px;line-height:26px;text-align:center;
  }
  .brand-name{
    position:absolute;left:0;right:0;top:70px;text-align:center;
    color:var(--blue);font-size:28px;font-weight:700;
  }
  .menu-icon{position:absolute;right:44px;top:56px;width:70px;height:46px}
  .menu-icon span{
    display:block;height:10px;border-radius:5px;margin-bottom:8px;
    background:linear-gradient(180deg,var(--cyan),var(--blue));
  }
  .now-playing{
    position:absolute;left:0;top:180px;width:670px;height:556px;
    background:linear-gradient(180deg,var(--cyan) 0%,var(--cyan-mid) 55%,#3a86cc 100%);
  }
  .equalizer{position:absolute;left:0;top:0;width:670px;height:556px}
  .share-button{position:absolute;left:576px;top:184px-180px}
  .frequency{
    position:absolute;left:0;right:0;top:288px;text-align:center;
    color:var(--white);font-size:74px;line-height:96px;
  }
  .station-row{position:absolute;left:0;right:0;top:418px;height:64px}
  .station-name{
    text-align:center;color:var(--cyan-text);font-size:52px;line-height:64px;
  }
  .station-arrow{position:absolute;top:14px;width:36px;height:36px}
  .station-arrow.prev{left:92px}
  .station-arrow.next{left:534px}
  .player-controls{
    position:absolute;left:0;top:736px;width:670px;height:188px;
    background:linear-gradient(180deg,#f4f5f7,var(--grey-bottom));
  }
  .tab-bar{
    position:absolute;left:0;top:924px;width:670px;height:180px;
    background:linear-gradient(180deg,var(--cyan),var(--cyan-mid) 60%,#3a86cc);
  }
  .tab{position:absolute;top:0;width:120px;height:180px;text-align:center}
  .tab svg{position:absolute;left:30px;top:40px;width:60px;height:60px}
  .tab-label{
    position:absolute;left:0;right:0;top:112px;color:var(--white);
    font-size:19px;font-weight:700;
  }
</style>
</head>
<body>
<main class="app-screen">
  <header class="app-header">
    <div class="back-button">Back</div>
    <div class="brand-name">Marrowind Radio</div>
    <div class="menu-icon"><span></span><span></span><span></span></div>
  </header>

  <section class="now-playing">
    <svg class="equalizer" viewBox="0 0 335 278" aria-hidden="true">
      <g fill="#ffffff">
        <!-- level cells -->
        <rect x="2" y="108" width="18" height="18"/><rect x="23" y="108" width="18" height="18"/><rect x="23" y="87" width="18" height="18"/>
        <rect x="44" y="108" width="18" height="18"/><rect x="65" y="108" width="18" height="18"/><rect x="65" y="87" width="18" height="18"/>
        <rect x="86" y="108" width="18" height="18"/><rect x="86" y="87" width="18" height="18"/><rect x="86" y="66" width="18" height="18"/><rect x="86" y="45" width="18" height="18"/>
        <rect x="107" y="108" width="18" height="18"/><rect x="107" y="87" width="18" height="18"/>
        <rect x="128" y="108" width="18" height="18"/>
        <rect x="149" y="108" width="18" height="18"/><rect x="149" y="87" width="18" height="18"/><rect x="149" y="66" width="18" height="18"/><rect x="149" y="45" width="18" height="18"/>
        <rect x="170" y="108" width="18" height="18"/><rect x="170" y="87" width="18" height="18"/><rect x="170" y="66" width="18" height="18"/>
        <rect x="191" y="108" width="18" height="18"/><rect x="191" y="87" width="18" height="18"/>
        <rect x="212" y="108" width="18" height="18"/><rect x="212" y="87" width="18" height="18"/><rect x="212" y="66" width="18" height="18"/>
        <rect x="233" y="108" width="18" height="18"/>
        <rect x="254" y="108" width="18" height="18"/><rect x="254" y="87" width="18" height="18"/><rect x="254" y="66" width="18" height="18"/>
        <rect x="275" y="108" width="18" height="18"/>
        <rect x="296" y="108" width="18" height="18"/>
        <rect x="317" y="108" width="18" height="18"/><rect x="317" y="87" width="18" height="18"/>
      </g>
      <g fill="#ffffff" opacity="0.55">
        <rect x="2" y="129" width="18" height="16"/><rect x="23" y="129" width="18" height="16"/><rect x="44" y="129" width="18" height="16"/><rect x="65" y="129" width="18" height="16"/>
        <rect x="86" y="129" width="18" height="16"/><rect x="107" y="129" width="18" height="16"/><rect x="128" y="129" width="18" height="16"/><rect x="149" y="129" width="18" height="16"/>
        <rect x="170" y="129" width="18" height="16"/><rect x="191" y="129" width="18" height="16"/><rect x="212" y="129" width="18" height="16"/><rect x="233" y="129" width="18" height="16"/>
        <rect x="254" y="129" width="18" height="16"/><rect x="275" y="129" width="18" height="16"/><rect x="296" y="129" width="18" height="16"/><rect x="317" y="129" width="18" height="16"/>
      </g>
      <g fill="#ffffff" opacity="0.15">
        <rect x="2" y="148" width="333" height="10"/>
      </g>
      <!-- share -->
      <circle cx="302" cy="16" r="14" fill="#ffffff"/>
      <g fill="var(--blue)"><circle cx="297" cy="16" r="2.6"/><circle cx="307" cy="11" r="2.6"/><circle cx="307" cy="21" r="2.6"/></g>
      <path d="M297 16 L307 11 M297 16 L307 21" stroke="var(--blue)" stroke-width="1.6"/>
    </svg>
    <div class="frequency">101.2</div>
    <div class="station-row">
      <svg class="station-arrow prev" viewBox="0 0 20 20" aria-hidden="true"><path d="M18 1 L2 10 L18 19Z" fill="var(--cyan-text)"/></svg>
      <div class="station-name">Radio Wren</div>
      <svg class="station-arrow next" viewBox="0 0 20 20" aria-hidden="true"><path d="M2 1 L18 10 L2 19Z" fill="var(--cyan-text)"/></svg>
    </div>
  </section>

  <section class="player-controls">
    <svg width="670" height="188" viewBox="0 0 670 188" aria-hidden="true">
      <defs>
        <linearGradient id="btnFill" x1="0" y1="0" x2="0" y2="1">
          <stop offset="0" stop-color="#4cc3db"/><stop offset="1" stop-color="#3176b5"/>
        </linearGradient>
      </defs>
      <rect x="104" y="22" width="462" height="10" rx="5" fill="var(--blue)"/>
      <rect x="104" y="22" width="148" height="10" rx="5" fill="var(--cyan)"/>
      <circle cx="252" cy="27" r="12" fill="var(--cyan-mid)" stroke="#ffffff" stroke-width="3"/>
      <!-- request / chat -->
      <circle cx="130" cy="110" r="34" fill="url(#btnFill)"/>
      <path d="M114 104 a12 9 0 1 1 10 9 l-6 5 l1 -6 a12 9 0 0 1 -5 -8z" fill="none" stroke="#fff" stroke-width="3"/>
      <path d="M128 114 a10 8 0 1 1 12 6 l3 5 l-7 -3" fill="none" stroke="#fff" stroke-width="3"/>
      <!-- rewind -->
      <circle cx="222" cy="110" r="34" fill="url(#btnFill)"/>
      <path d="M222 98 L206 110 L222 122Z M238 98 L222 110 L238 122Z" fill="#fff"/>
      <!-- play -->
      <circle cx="336" cy="110" r="54" fill="url(#btnFill)"/>
      <circle cx="336" cy="110" r="36" fill="none" stroke="#fff" stroke-width="7"/>
      <path d="M326 92 L354 110 L326 128Z" fill="#fff"/>
      <!-- forward -->
      <circle cx="446" cy="110" r="34" fill="url(#btnFill)"/>
      <path d="M430 98 L446 110 L430 122Z M446 98 L462 110 L446 122Z" fill="#fff"/>
      <!-- favourite -->
      <circle cx="538" cy="110" r="34" fill="url(#btnFill)"/>
      <path d="M538 92 L543 105 L557 105 L546 114 L550 128 L538 120 L526 128 L530 114 L519 105 L533 105Z" fill="#fff"/>
    </svg>
  </section>

  <nav class="tab-bar">
    <div class="tab" style="left:26px">
      <svg viewBox="0 0 60 60" aria-hidden="true" fill="none" stroke="#fff" stroke-width="4" stroke-linecap="round">
        <circle cx="30" cy="30" r="4" fill="#fff" stroke="none"/>
        <path d="M20 20 a14 14 0 0 0 0 20 M40 20 a14 14 0 0 1 0 20 M11 12 a26 26 0 0 0 0 36 M49 12 a26 26 0 0 1 0 36"/>
      </svg>
      <div class="tab-label">Stations</div>
    </div>
    <div class="tab" style="left:152px">
      <svg viewBox="0 0 60 60" aria-hidden="true"><circle cx="24" cy="22" r="13" fill="none" stroke="#fff" stroke-width="6"/><path d="M33 32 L50 50" stroke="#fff" stroke-width="9" stroke-linecap="round"/></svg>
      <div class="tab-label">Search</div>
    </div>
    <div class="tab" style="left:284px">
      <svg viewBox="0 0 60 60" aria-hidden="true" style="left:14px;width:92px;top:36px;height:66px"><rect x="4" y="12" width="52" height="36" fill="#fff"/><path d="M4 12 L30 34 L56 12 M4 48 L24 29 M56 48 L36 29" stroke="var(--blue)" stroke-width="2" fill="none"/></svg>
      <div class="tab-label">Message</div>
    </div>
    <div class="tab" style="left:420px">
      <svg viewBox="0 0 60 60" aria-hidden="true" fill="none" stroke="#fff" stroke-width="5"><circle cx="30" cy="33" r="18"/><path d="M30 23 V34 H38" stroke-width="4"/><path d="M10 16 a9 9 0 0 1 12 -8 M50 16 a9 9 0 0 0 -12 -8" stroke-width="5"/></svg>
      <div class="tab-label">Alarm</div>
    </div>
    <div class="tab" style="left:530px">
      <svg viewBox="0 0 60 60" aria-hidden="true"><rect x="4" y="26" width="12" height="12" fill="#fff"/><rect x="24" y="26" width="12" height="12" fill="#fff"/><rect x="44" y="26" width="12" height="12" fill="#fff"/></svg>
      <div class="tab-label">More</div>
    </div>
  </nav>
</main>
</body>
</html>
```